Talvero Engineering & Management Services Website

A professional website design that outlines Engineering and Management Services. The website is to be colour coordinated with the current logo (see attached). The webpage needs to be compatible with Wordpress to allow for easy changes to be made to the website for the user.
Required tabs for the page include:
- Civil Engineering
- Structural Engineering
- Project Management
- Business Management
- Project Controls
- Drafting
- Contact Us

Clean and efficient website that matches the services provided by the business.

Target Market(s)

New Customers to a very competitive market

Industry/Entity Type

Engineering

Number of Pages Required

5+ page

Requirements
Must have
• Clean with large stock photos

```html
<!DOCTYPE html>
<html lang="en">
<head>
<meta charset="utf-8">
<title>Talvero Engineering &amp; Management Services</title>
<link href="https://fonts.googleapis.com/css2?family=Oswald:wght@400;500;600&family=Open+Sans:wght@400;600;700&display=swap" rel="stylesheet">
<style>
:root{
  --orange:#f07a22;
  --orange-dark:#d9651a;
  --ink:#3a3a3a;
  --muted:#8a8a8a;
  --light:#f1f1f1;
  --footer:#2b2b2b;
  --footer-deep:#1f1f1f;
  --white:#ffffff;
}
*{box-sizing:border-box;margin:0;padding:0}
html,body{width:723px;height:1200px;overflow:hidden;background:var(--white)}
body{font-family:"Open Sans",Arial,sans-serif;color:var(--ink);font-size:7px;line-height:1.5}
.site-header{height:78px;display:flex;align-items:center;justify-content:space-between;padding:0 40px}
.brand{display:flex;align-items:center;gap:10px}
.brand-dot{width:42px;height:42px;border-radius:50%;background:var(--orange)}
.brand-name{font-weight:700;font-size:15px;line-height:1.15;color:var(--ink);width:240px}
.header-contact{display:flex;flex-direction:column;align-items:flex-end;gap:4px}
.call-label{font-size:8px;color:var(--muted)}
.call-number{font-size:15px;font-weight:700;color:var(--orange);line-height:1}
.social{display:flex;gap:4px}
.social span{width:11px;height:11px;border-radius:50%;background:#bdbdbd}
.main-nav{height:22px;background:var(--orange);display:flex;justify-content:center;align-items:center;gap:15px}
.main-nav a{color:var(--white);text-decoration:none;font-size:7.2px;font-weight:600;letter-spacing:.2px}
.hero{position:relative;height:262px;background:linear-gradient(180deg,#a9b3bc 0%,#d6dadd 45%,#c2c2c0 75%,#8f8d88 100%);display:flex;flex-direction:column;align-items:center;padding-top:68px}
.hero-title{font-family:"Oswald",Arial,sans-serif;font-weight:500;font-size:38px;letter-spacing:4px;color:#2a2a2a;line-height:1}
.hero-sub{font-size:9px;color:#333;margin-top:6px}
.btn{margin-top:12px;background:#2b2b2b;color:var(--white);font-size:7.5px;font-weight:700;padding:6px 12px;border-radius:2px}
.hero-dots{position:absolute;bottom:44px;display:flex;gap:4px}
.hero-dots span{width:6px;height:6px;border-radius:50%;background:#fff;opacity:.7}
.hero-dots span.on{background:var(--orange);opacity:1}
.services{display:flex;justify-content:center;gap:6px;margin-top:-36px;position:relative}
.service{width:104px}
.service-photo{height:70px;border:3px solid var(--white);background:linear-gradient(160deg,#c9d3dc,#8e9aa4)}
.service-name{font-size:8.5px;font-weight:700;margin-top:6px;line-height:1.2;color:#2b2b2b}
.welcome{text-align:center;padding:26px 70px 0}
.welcome h2{font-family:"Oswald",Arial,sans-serif;font-size:12px;font-weight:500;color:var(--orange);letter-spacing:.5px}
.rule{width:70px;height:1px;background:#ccc;margin:6px auto 10px}
.welcome p{color:var(--muted);font-size:6.6px;margin-bottom:9px}
.testimonials{margin-top:30px;background:var(--light);height:240px;padding:22px 70px 0;text-align:center}
.testimonials h2{font-family:"Oswald",Arial,sans-serif;font-size:11px;font-weight:500;color:var(--orange)}
.intro{color:var(--muted);font-size:6.6px;margin:4px 60px 0}
.quotes{display:flex;gap:26px;margin-top:20px}
.quote{flex:1}
.quote-mark{font-family:"Oswald",Arial,sans-serif;font-size:22px;color:#c9c9c9;line-height:1}
.quote p{color:var(--muted);font-size:6.6px;margin-top:4px}
.quote cite{display:block;font-style:normal;font-weight:700;font-size:7px;margin-top:10px;color:var(--ink)}
.site-footer{position:relative;background:var(--footer);height:290px;margin-top:18px;padding:52px 40px 0;color:#cfcfcf}
.footer-badge{position:absolute;top:-18px;left:50%;margin-left:-18px;width:36px;height:36px;border-radius:50%;background:var(--orange);border:3px solid var(--footer)}
.footer-cols{display:flex;gap:30px}
.footer-col{flex:1}
.footer-col h3{font-size:8px;font-weight:700;color:var(--white);margin-bottom:10px}
.post{display:flex;gap:6px;margin-bottom:12px}
.post-thumb{width:22px;height:22px;background:#555;flex:none}
.post p{font-size:6.4px;color:#bdbdbd}
.contact-line{display:flex;gap:6px;align-items:flex-start;font-size:6.4px;margin-bottom:8px}
.contact-line svg{flex:none}
.links li{list-style:none;font-size:6.6px;margin-bottom:4px}
.footer-bar{position:absolute;left:0;right:0;bottom:0;height:28px;background:var(--footer-deep);display:flex;align-items:center;justify-content:space-between;padding:0 40px;font-size:6.4px;color:#9a9a9a}
.footer-bar .social span{background:#666}
</style>
</head>
<body>
<header class="site-header">
  <div class="brand">
    <div class="brand-dot"></div>
    <div class="brand-name">Talvero Engineering &amp; Management Services</div>
  </div>
  <div class="header-contact">
    <div class="call-label">Questions? Call</div>
    <div class="call-number">1-888-555-0142</div>
    <div class="social"><span></span><span></span><span></span><span></span></div>
  </div>
</header>
<nav class="main-nav">
  <a>HOME</a><a>CIVIL ENGINEERING</a><a>STRUCTURAL ENGINEERING</a><a>PROJECT MANAGEMENT</a><a>BUSINESS MANAGEMENT</a><a>PROJECT CONTROLS</a><a>DRAFTING</a><a>CONTACT US</a>
</nav>
<section class="hero" role="img" aria-label="Engineers inspecting large industrial storage tanks under a cloudy sky">
  <h1 class="hero-title">LOREM IPSUM DOLOR SIT AMET</h1>
  <div class="hero-sub">Sed ut perspiciatis unde omnis iste natus error sit voluptatem accusantium</div>
  <div class="btn">LEARN MORE</div>
  <div class="hero-dots"><span class="on"></span><span></span><span></span><span></span></div>
</section>
<section class="services">
  <div class="service"><div class="service-photo" role="img" aria-label="Civil engineering site work"></div><div class="service-name">Civil<br>Engineering</div></div>
  <div class="service"><div class="service-photo" role="img" aria-label="Structural steel framework"></div><div class="service-name">Structural<br>Engineering</div></div>
  <div class="service"><div class="service-photo" role="img" aria-label="Project team reviewing plans"></div><div class="service-name">Project<br>Management</div></div>
  <div class="service"><div class="service-photo" role="img" aria-label="Business meeting"></div><div class="service-name">Business<br>Management</div></div>
  <div class="service"><div class="service-photo" role="img" aria-label="Project control charts"></div><div class="service-name">Project<br>Controls</div></div>
  <div class="service"><div class="service-photo" role="img" aria-label="Technical drafting table"></div><div class="service-name">Drafting</div></div>
</section>
<section class="welcome">
  <h2>WELCOME TO TALVERO ENGINEERING AND MANAGEMENT SERVICES</h2>
  <div class="rule"></div>
  <p>Lorem ipsum dolor sit amet, consectetur adipiscing elit, sed do eiusmod tempor incididunt ut labore et dolore magna aliqua. Ut enim ad minim veniam, quis nostrud exercitation ullamco laboris nisi ut aliquip ex ea commodo consequat. Duis aute irure dolor in reprehenderit in voluptate velit esse cillum dolore eu fugiat nulla pariatur. Excepteur sint occaecat cupidatat non proident, sunt in culpa qui officia deserunt mollit anim id est laborum.</p>
  <p>Sed ut perspiciatis unde omnis iste natus error sit voluptatem accusantium doloremque laudantium, totam rem aperiam, eaque ipsa quae ab illo inventore veritatis et quasi architecto beatae vitae dicta sunt explicabo.</p>
</section>
<section class="testimonials">
  <h2>WHAT OUR PEOPLE ARE SAYING</h2>
  <p class="intro">Lorem ipsum dolor sit amet, consectetur adipiscing elit, sed do eiusmod tempor incididunt ut labore et dolore magna aliqua. Ut enim ad minim veniam.</p>
  <div class="quotes">
    <div class="quote"><div class="quote-mark">&ldquo;</div><p>Sed ut perspiciatis unde omnis iste natus error sit voluptatem accusantium doloremque laudantium, totam rem aperiam, eaque ipsa quae ab illo inventore veritatis et quasi architecto beatae vitae dicta sunt explicabo. Nemo enim ipsam voluptatem quia voluptas sit aspernatur.</p><cite>Dana</cite></div>
    <div class="quote"><div class="quote-mark">&ldquo;</div><p>Sed ut perspiciatis unde omnis iste natus error sit voluptatem accusantium doloremque laudantium, totam rem aperiam, eaque ipsa quae ab illo inventore veritatis et quasi architecto beatae vitae dicta sunt explicabo. Nemo enim ipsam voluptatem quia voluptas sit aspernatur.</p><cite>Dana</cite></div>
    <div class="quote"><div class="quote-mark">&ldquo;</div><p>Sed ut perspiciatis unde omnis iste natus error sit voluptatem accusantium doloremque laudantium, totam rem aperiam, eaque ipsa quae ab illo inventore veritatis et quasi architecto beatae vitae dicta sunt explicabo. Nemo enim ipsam voluptatem quia voluptas sit aspernatur.</p><cite>Dana</cite></div>
  </div>
</section>
<footer class="site-footer">
  <div class="footer-badge"></div>
  <div class="footer-cols">
    <div class="footer-col">
      <h3>RECENT NEWS</h3>
      <div class="post"><div class="post-thumb"></div><p>Nemo enim ipsam voluptatem quia voluptas sit aspernatur aut odit.</p></div>
      <div class="post"><div class="post-thumb"></div><p>Nemo enim ipsam voluptatem quia voluptas sit aspernatur aut odit.</p></div>
    </div>
    <div class="footer-col">
      <h3>RECENT BLOG</h3>
      <div class="post"><div class="post-thumb"></div><p>Nemo enim ipsam voluptatem quia voluptas sit aspernatur aut odit.</p></div>
      <div class="post"><div class="post-thumb"></div><p>Nemo enim ipsam voluptatem quia voluptas sit aspernatur aut odit.</p></div>
    </div>
    <div class="footer-col">
      <h3>CONTACT US</h3>
      <div class="contact-line"><svg width="8" height="10" viewBox="0 0 8 10"><path d="M4 0a4 4 0 0 0-4 4c0 3 4 6 4 6s4-3 4-6a4 4 0 0 0-4-4z" fill="var(--orange)"/><circle cx="4" cy="4" r="1.4" fill="var(--footer)"/></svg><span>214, Harlow Street, Suite 6,<br>Northgate, 40210</span></div>
      <div class="contact-line"><svg width="8" height="8" viewBox="0 0 8 8"><path d="M1 0h2l1 2-1 1a5 5 0 0 0 2 2l1-1 2 1v2c0 .6-.4 1-1 1A7 7 0 0 1 0 1c0-.6.4-1 1-1z" fill="var(--orange)"/></svg><span>Phone: 1-888-555-0142</span></div>
      <div class="contact-line"><svg width="9" height="7" viewBox="0 0 9 7"><rect width="9" height="7" rx="1" fill="var(--orange)"/><path d="M0 1l4.5 3L9 1" stroke="var(--footer)" fill="none"/></svg><span>info@talvero-ems.com</span></div>
    </div>
    <div class="footer-col">
      <h3>QUICK LINKS</h3>
      <ul class="links"><li>Civil Engineering</li><li>Structural Engineering</li><li>Project Management</li><li>Business Management</li><li>Project Controls</li><li>Drafting</li></ul>
    </div>
  </div>
  <div class="footer-bar">
    <span>&copy; 2015 Talvero. All Rights Reserved &nbsp;|&nbsp; Terms and Conditions &nbsp;|&nbsp; Privacy Policy &nbsp;|&nbsp; Terms of Use</span>
    <div class="social"><span></span><span></span><span></span></div>
  </div>
</footer>
</body>
</html>
```